RHS Trifold Brochure

Would like a Trifold Brochure to use for marketing purposes. The company, Reliable Home Solutions is a Handyman Service that offers Residential Home Repairs, Commercial Repairs, Drain Cleaning, Carpet Cleaning and Water Extraction.

I am attaching some pdf files to use as potential verbage and a copy of our business card and logo image file.

Would like to portray a professional image that sets us apart from a "mom and pops" type handyman service.

Industry/Entity Type

Marketing

```html
<!DOCTYPE html>
<html lang="en">
<head>
<meta charset="utf-8">
<title>Reliable Home Solutions – Trifold Brochure</title>
<link href="https://fonts.googleapis.com/css2?family=Mulish:ital,wght@0,400;0,600;0,700;0,800;1,800&display=swap" rel="stylesheet">
<style>
:root{
  --navy:#1b2d52;
  --navy-deep:#111f3b;
  --blue:#1f4e96;
  --sky:#2c7fd0;
  --ink:#4b4f55;
  --grey:#6d7076;
  --line:#a3a8b0;
  --paper:#ffffff;
  --paper-soft:#eef0f3;
  --stage:#ebe8e3;
}
*{box-sizing:border-box;margin:0;padding:0}
html,body{width:1200px;height:518px;overflow:hidden;background:var(--stage);font-family:"Mulish",sans-serif;color:var(--ink)}
.canvas{position:relative;width:1200px;height:518px}

.brochure{position:absolute;display:flex;background:var(--paper);box-shadow:0 2px 6px rgba(0,0,0,.25)}
.brochure--outside{left:24px;top:22px;width:562px;height:436px}
.brochure--inside{left:614px;top:62px;width:562px;height:434px}
.panel{position:relative;width:187.33px;height:100%;overflow:hidden;background:linear-gradient(180deg,#fff 0%,var(--paper-soft) 100%)}
.panel+.panel{border-left:1px solid #d7dade}

.top-strip{position:absolute;left:0;top:0;width:100%;height:9px;background:var(--navy)}
.tab{position:absolute;left:12px;right:12px;top:18px;height:26px;border:2px solid var(--line);border-left:6px solid var(--line);border-radius:9px;display:flex;align-items:center;justify-content:center;font-weight:700;font-size:13px;color:var(--navy);background:#fff}

.body{font-size:5.4px;line-height:1.42;text-align:justify;color:var(--ink)}
.lead{font-weight:700;text-align:center;color:var(--blue)}
.sub{font-weight:800;font-size:6.6px;color:var(--navy);margin-top:4px}
.photo{position:absolute}

.phone-band{position:absolute;left:0;bottom:0;width:100%;height:27px;background:var(--navy);color:#fff;font-weight:800;font-size:14px;display:flex;align-items:center;padding-left:14px}
.phone-badge{position:absolute;width:38px;height:34px}

.brand{display:flex;flex-direction:column;align-items:center;font-weight:800;line-height:1.05;text-align:center}

/* outside: left panel */
.outside-intro .headline{position:absolute;left:10px;right:10px;top:56px;font-weight:700;font-size:10.5px;line-height:1.3;text-align:center;color:#55595f}
.outside-intro .body{position:absolute;left:12px;right:12px;top:102px;font-size:5.6px}
.outside-intro .photo{left:0;top:204px;width:100%;height:172px;background:linear-gradient(160deg,#f3f3f3 0%,#d9d4cf 35%,#b89c8a 60%,#8d8d8f 85%,#d9d9da 100%)}
.call-band{position:absolute;left:0;bottom:0;width:100%;height:60px;background:linear-gradient(160deg,#7a7d82 0%,#55585d 100%);color:#fff;font-weight:800;padding:10px 0 0 14px}
.call-band .call{font-size:14px}
.call-band .num{font-size:14.5px;margin-top:4px;display:flex;align-items:center;gap:4px}

/* outside: hero photo across middle and right panels */
.hero{position:absolute;z-index:3;left:187.33px;top:0;width:374.67px;height:242px;background:linear-gradient(180deg,#33455f 0%,#4d607a 22%,#6b5446 40%,#8d4f38 58%,#9a7760 78%,#b9b0a2 100%)}
.social{position:absolute;display:flex;gap:3px;z-index:4}
.social span{width:12px;height:12px;border-radius:2px;background:var(--sky)}
.outside-call .strip{position:absolute;left:0;top:242px;width:100%;height:20px;background:var(--navy)}
.outside-call .social{right:10px;top:246px}
.outside-call .call{position:absolute;left:14px;top:275px;display:flex;gap:8px;align-items:center}
.outside-call .call-text{font-weight:800;color:var(--navy)}
.outside-call .call-text .c1{font-size:14px;padding-left:14px}
.outside-call .call-text .c2{font-size:14.5px;margin-top:4px}
.contact-block{position:absolute;left:0;bottom:0;width:100%;height:94px;background:var(--navy);color:#fff;padding:10px 12px 0}
.contact-block .brand{font-size:11px}
.contact-block .brand small{font-size:6px;font-weight:600;letter-spacing:.5px;margin-top:2px}
.contact-rows{margin-top:8px;font-size:5.6px;line-height:1.7;color:#dfe4ee}
.contact-rows div{display:flex;align-items:center;gap:4px}
.contact-rows .pair{justify-content:space-between}
.contact-rows svg{width:6px;height:6px;flex:none}

.outside-cover .strip{position:absolute;left:0;top:242px;width:100%;height:20px;background:var(--navy-deep);color:#fff;font-weight:800;font-style:italic;font-size:9.5px;display:flex;align-items:center;justify-content:center}
.outside-cover .brand{position:absolute;left:10px;right:10px;top:282px;color:var(--navy);font-size:17px}
.outside-cover .brand small{font-size:7px;font-weight:700;letter-spacing:1.5px;margin-top:4px}
.outside-cover .tools-area{position:absolute;left:0;bottom:0;width:100%;height:94px;background:var(--navy)}
.outside-cover .tools-area .photo{left:14px;top:8px;width:159px;height:52px;border-radius:4px;background:linear-gradient(135deg,#8a5b34 0%,#a87545 45%,#6b4528 100%)}
.outside-cover .tools-area .num{position:absolute;left:0;right:0;bottom:8px;text-align:center;color:#fff;font-weight:800;font-size:14.5px}

/* inside */
.inside .content{position:absolute;left:12px;right:12px;top:50px}
.services{display:grid;grid-template-columns:1fr 1fr;column-gap:6px;margin-top:7px}
.services h4{font-size:6.2px;font-weight:800;color:var(--blue);margin-bottom:2px}
.services ul{list-style:none;font-size:5.2px;line-height:1.55;margin-bottom:7px}
.services .left li::before{content:"•";color:var(--navy);margin-right:2px}
.services .right{text-align:right}
.services .right li::after{content:"•";color:var(--navy);margin-left:2px}
.handyman .photo{left:10px;top:318px;width:86px;height:80px;border-radius:4px;background:linear-gradient(135deg,#d98b3a 0%,#c9bfb2 50%,#7d8a9a 100%)}
.handyman .phone-badge,.carpet .phone-badge{right:6px;bottom:14px}

.ticks{list-style:none;font-size:5.3px;line-height:1.6;margin-top:2px}
.ticks li{display:flex;align-items:center;gap:3px}
.ticks svg{width:5px;height:5px}
.why{display:flex;gap:4px;align-items:flex-start}
.drain .why .photo{position:relative;width:62px;height:46px;flex:none;margin-top:2px;background:linear-gradient(135deg,#e3e8ee 0%,#7f9fc6 55%,#33507e 100%)}
.emergency{position:absolute;left:36px;width:116px;top:334px;height:44px;border-radius:4px;background:linear-gradient(90deg,#9fb9d3 0%,#4d81b8 45%,#1f4e96 100%);color:#fff;font-weight:800;text-align:right;padding:4px 8px;line-height:1}
.emergency .e1{font-size:14px}.emergency .e2{font-size:12px}.emergency .e3{font-size:6px}
.drain .brand{position:absolute;left:0;right:0;top:384px;color:var(--navy);font-size:10.5px}
.drain .brand small{font-size:5.5px;letter-spacing:1px;margin-top:2px}
.drain .foot{position:absolute;left:0;bottom:0;width:100%;height:14px}

.available{font-weight:800;font-size:10px;line-height:1.15;text-align:center;color:var(--blue);margin-top:6px}
.gallery{position:absolute;left:8px;right:8px;top:300px;height:90px;display:grid;grid-template-columns:1fr 1fr;grid-template-rows:1fr 1fr;gap:2px}
.gallery div{border-radius:1px}
.g-before{background:linear-gradient(90deg,#a4896a 0%,#b9a587 50%,#d6cbb8 100%);color:#fff;font-size:5px;font-weight:700;display:flex;justify-content:space-around;padding-top:4px}
.g-family{grid-row:span 2;background:linear-gradient(180deg,#eae5df 0%,#cdbfb0 60%,#e8e2da 100%)}
.g-flood{background:linear-gradient(180deg,#6fa6cf 0%,#9cb7c7 100%)}
.carpet .social{left:36px;top:393px}
</style>
</head>
<body>
<div class="canvas">

  <section class="brochure brochure--outside" aria-label="Brochure outside spread">
    <div class="panel outside-intro">
      <div class="top-strip"></div>
      <div class="tab">Riverbend Maintenance</div>
      <p class="headline">The Service You Can Need.<br>The Quality you Expect .<br>Prices you can Afford!!!</p>
      <p class="body">Reliable Home Solutions is the professional answer to your all of your home maintenance needs. Our courteous and knowledgable staff have the skills necessary to resolve your issues at a price that you can afford. Reliable Home Solutions offers Handyman Services, Carpet Cleaning, Tile &amp; Grout Cleaning and Drain Cleaning Services. If you are looking for an affordable solution to your home upkeep needs then give Reliable Home Solutions a Call Today and see what we can do for you!!!</p>
      <div class="photo" role="img" aria-label="Photo of hands holding a small model house"></div>
      <div class="call-band">
        <div class="call">Call Today!!!</div>
        <div class="num"><svg width="12" height="12" viewBox="0 0 24 24"><circle cx="12" cy="12" r="11" fill="none" stroke="#fff" stroke-width="2"/><path d="M8 6l2 3-1.5 1.5a8 8 0 0 0 5 5L15 14l3 2-1 2.5c-5 0-10-5-10-10z" fill="#fff"/></svg>(555) 014-2280</div>
      </div>
    </div>

    <div class="hero" role="img" aria-label="Photo of a handyman on a ladder cleaning the gutter of a brick house"></div>

    <div class="panel outside-call" style="background:#fff">
      <div class="strip"></div>
      <div class="social" aria-hidden="true"><span></span><span></span><span></span></div>
      <div class="call">
        <svg width="34" height="34" viewBox="0 0 40 40" aria-hidden="true">
          <circle cx="26" cy="12" r="10" fill="#fff" stroke="var(--sky)" stroke-width="1.5"/>
          <text x="26" y="15" font-size="8" font-weight="800" fill="var(--sky)" text-anchor="middle" font-family="Mulish,sans-serif">24/7</text>
          <path d="M4 14c2-3 5-3 6 0l1 4-3 2c1 4 4 7 8 9l2-3 4 1c3 1 3 4 0 6-8 3-21-10-18-19z" fill="var(--sky)"/>
        </svg>
        <div class="call-text"><div class="c1">Call Today!!!</div><div class="c2">(555) 014-2280</div></div>
      </div>
      <div class="contact-block">
        <div class="brand">Reliable Home Solutions<small>HANDYMAN &amp; CLEANING</small></div>
        <div class="contact-rows">
          <div class="pair"><span style="display:flex;gap:4px;align-items:center"><svg viewBox="0 0 10 10"><path d="M5 0a3.5 3.5 0 0 0-3.5 3.5C1.5 6 5 10 5 10s3.5-4 3.5-6.5A3.5 3.5 0 0 0 5 0z" fill="#fff"/></svg>120 Cedar Lane</span><span style="display:flex;gap:4px;align-items:center"><svg viewBox="0 0 10 10"><path d="M2 1l2 2-1 1a5 5 0 0 0 3 3l1-1 2 2-1 1.5C4 9 1 6 .5 2z" fill="#fff"/></svg>555.014.2280</span></div>
          <div class="pair"><span style="padding-left:10px">Riverbend, KS</span><span style="display:flex;gap:4px;align-items:center"><svg viewBox="0 0 10 10"><rect x="1" y="2" width="8" height="6" fill="#fff"/></svg>555.014.2281</span></div>
          <div><svg viewBox="0 0 10 10"><rect x="0.5" y="2" width="9" height="6" fill="none" stroke="#fff"/><path d="M.5 2l4.5 3.5L9.5 2" fill="none" stroke="#fff"/></svg>info@reliablehomesol.com</div>
          <div><svg viewBox="0 0 10 10"><circle cx="5" cy="5" r="4" fill="none" stroke="#fff"/></svg>www.reliablehomesol.com</div>
        </div>
      </div>
    </div>

    <div class="panel outside-cover" style="background:#fff">
      <div class="strip">Service You Can Count On!!!</div>
      <div class="brand">Reliable Home Solutions<small>HANDYMAN &amp; CLEANING</small></div>
      <div class="tools-area">
        <div class="photo" role="img" aria-label="Photo of a leather tool belt full of hand tools"></div>
        <div class="num">(555) 014-2280</div>
      </div>
    </div>
  </section>

  <section class="brochure brochure--inside inside" aria-label="Brochure inside spread">
    <div class="panel handyman">
      <div class="top-strip"></div>
      <div class="tab">Handyman Services</div>
      <div class="content">
        <p class="lead" style="font-size:7.8px;line-height:1.25">Reliable Home Solutions<br>Handyman Services, When you<br>just need to get it done!!!</p>
        <p class="body" style="margin-top:5px">Reliable Home Solutions is the answer to your home repair needs. Our staff of experienced technicians have the skills necessary to resolve all of your repair and maintenance issues. Minor Electrical, Plumbing, Heating and Air Conditioning, Honey Do Lists, Painting, Drywall Repair, Locks, Doors, Screens and Windows, Exterior Clean Up, Deck and Siding Repair, Appliance Repairs, Caulking, Tile...you name it we've got you covered <b>Call Us Today</b> to see how we can help you!!!</p>
        <div class="services">
          <div class="left">
            <h4>Plumbing</h4>
            <ul><li>Faucets</li><li>Sinks</li><li>Toilets</li><li>Garbage Disposals</li><li>Hot Water Tanks</li><li>Shut Off Valves</li><li>Leaks</li></ul>
            <h4>HVAC &amp; Appliances</h4>
            <ul><li>Air Conditioning</li><li>Furnaces</li><li>Hot Water Heaters</li><li>Fridges</li><li>Stoves</li><li>Dishwashers</li></ul>
          </div>
          <div class="right">
            <h4>Interior Services</h4>
            <ul><li>Painting</li><li>Drywall Repair</li><li>Screens/Windows</li><li>Locks</li><li>Tile Repair</li><li>Tile/Grout Cleaning</li><li>Caulking</li><li>Handrails</li></ul>
            <h4>Exterior Services</h4>
            <ul><li>Gutter Cleaning</li><li>Power Washing</li><li>Deck Repairs</li><li>Staining/Sealing</li><li>Wood Rot Repairs</li><li>Minor Roof Repairs</li></ul>
            <h4>Electrical</h4>
            <ul><li>Lighting</li><li>Outlets</li><li>Switches</li><li>GFCI</li><li>Ceiling Fans</li></ul>
          </div>
        </div>
      </div>
      <div class="photo" role="img" aria-label="Illustration of a house outline made of tools"></div>
      <div class="phone-band">(555) 014-2280</div>
      <svg class="phone-badge" viewBox="0 0 40 40" aria-hidden="true">
        <circle cx="26" cy="12" r="10" fill="#fff" stroke="var(--sky)" stroke-width="1.5"/>
        <text x="26" y="15" font-size="8" font-weight="800" fill="var(--sky)" text-anchor="middle" font-family="Mulish,sans-serif">24/7</text>
        <path d="M4 14c2-3 5-3 6 0l1 4-3 2c1 4 4 7 8 9l2-3 4 1c3 1 3 4 0 6-8 3-21-10-18-19z" fill="var(--sky)"/>
      </svg>
    </div>

    <div class="panel drain">
      <div class="top-strip"></div>
      <div class="tab">Drain Cleaning</div>
      <div class="content">
        <p class="lead" style="font-size:7px">Drain Cleaning Services You Can Count On!!!</p>
        <p class="body" style="margin-top:3px">A clogged sewer line is an emergency that needs to be dealt with. Reliable Home Solutions is your local source for all of your drain cleaning needs. Our Expert Technicians are available 24 Hours a day, 7 Days a week. Whether it is a backed up toilet, a tub drain, a sink or the main sewer line... Drains are what we do!!! Give us a <b>Call Today</b> to see how we can help.</p>
        <p class="sub">Why Reliable Home Solutions?</p>
        <div class="why">
          <ul class="ticks">
            <li><svg viewBox="0 0 10 10"><path d="M1 5l3 3 5-7" fill="none" stroke="var(--navy)" stroke-width="2"/></svg>Locally Owned &amp; Operated</li>
            <li><svg viewBox="0 0 10 10"><path d="M1 5l3 3 5-7" fill="none" stroke="var(--navy)" stroke-width="2"/></svg>Quality Drain Cleaning Services</li>
            <li><svg viewBox="0 0 10 10"><path d="M1 5l3 3 5-7" fill="none" stroke="var(--navy)" stroke-width="2"/></svg>24 Hour Emergency Drain Service</li>
            <li><svg viewBox="0 0 10 10"><path d="M1 5l3 3 5-7" fill="none" stroke="var(--navy)" stroke-width="2"/></svg>Affordable Pricing</li>
            <li><svg viewBox="0 0 10 10"><path d="M1 5l3 3 5-7" fill="none" stroke="var(--navy)" stroke-width="2"/></svg>Warranty Provided</li>
          </ul>
          <div class="photo" role="img" aria-label="Photo of a technician clearing a drain under a sink"></div>
        </div>
        <p class="sub">Diagnostic Capabilities</p>
        <p class="body">Our expert technicians have the knowledge and resources necessary to ensure a proper diagnosis of your drain problem. Our technicians will be able to determine where the blockage is, how to clear the blockage and in some cases what is causing the blockage.</p>
        <p class="sub">The Right Equipment</p>
        <p class="body">Half the battle is having the right equipment for the job. Our technicians are equipped with the machinery necessary to clear your blocked sewer line whether it is a bathroom lavatory or the main sewer line. Reliable Home Solutions, we are the right tool for the job!</p>
        <p class="sub">Service Area</p>
        <p class="body">Reliable Home Solutions services Cedar County and surrounding area's (Additional charges apply outside Cedar County). We service Residential Homes, Commercial Buildings, Apartment Complexes and Rental Properties of all types. Call Today to see what Reliable Home Solutions can do for you!!!</p>
      </div>
      <div class="emergency" role="img" aria-label="Photo of a sink drain behind the 24 hour emergency service notice"><div class="e1">24</div><div class="e2">HOUR</div><div class="e3">EMERGENCY<br>SERVICE</div></div>
      <div class="brand">Reliable Home Solutions<small>HANDYMAN &amp; CLEANING</small></div>
      <svg class="foot" viewBox="0 0 187 14" preserveAspectRatio="none" aria-hidden="true"><path d="M0 0h70l23 8 23-8h71v14H0z" fill="var(--navy)"/></svg>
    </div>

    <div class="panel carpet">
      <div class="top-strip"></div>
      <div class="tab">Carpet Cleaning</div>
      <div class="content">
        <p class="lead" style="font-size:8px">It's Your Carpet, How Clean is it?</p>
        <p class="body" style="margin-top:3px">Carpet is one of the most used items in our household and yet is often the most ignored. Dirt, Sand, Food, Dander, Dead Skin, Hair, Grease and oil all build up over time. Sure you vacuum but is it doing enough? The answer is no! Let us take care of your carpet cleaning needs with our experienced technicians and the right equipment for the job.</p>
        <p class="sub">Tile &amp; Grout Cleaning. The Results<br>Speak for Themselves!!!</p>
        <p class="body">It only takes once before you are a believer! Tile and grout build up layers of dirt and grime over time. Mopping and scrubbing go a long way but from time to time they need a deep clean. That is where Reliable Home Solutions comes in. Regardless of where the tile is we can make a difference for you!</p>
        <p class="sub">Emergency Water Extraction!!!</p>
        <p class="body">Water does serious damage. When there is an emergency, timing is of the essence. When that pipe breaks or a back up occurs call us and we'll be there. Our knowledgable staff and is equipped with the resources to give you the best chance of salvaging your carpet after a major water issue. <b>Call Today</b> to see how we can help!!!</p>
        <p class="available">We are Available 24/7 for<br>Emergency Water Extraction!!!</p>
      </div>
      <div class="gallery">
        <div class="g-before" role="img" aria-label="Before and after photo of a cleaned carpet"><span>BEFORE</span><span>AFTER</span></div>
        <div class="g-family" role="img" aria-label="Photo of a parent and baby on a clean carpet"></div>
        <div class="g-flood" role="img" aria-label="Photo of a flooded room"></div>
      </div>
      <div class="social" aria-hidden="true"><span></span><span></span><span></span></div>
      <div class="phone-band">(555) 014-2280</div>
      <svg class="phone-badge" viewBox="0 0 40 40" aria-hidden="true">
        <circle cx="26" cy="12" r="10" fill="#fff" stroke="var(--sky)" stroke-width="1.5"/>
        <text x="26" y="15" font-size="8" font-weight="800" fill="var(--sky)" text-anchor="middle" font-family="Mulish,sans-serif">24/7</text>
        <path d="M4 14c2-3 5-3 6 0l1 4-3 2c1 4 4 7 8 9l2-3 4 1c3 1 3 4 0 6-8 3-21-10-18-19z" fill="var(--sky)"/>
      </svg>
    </div>
  </section>

</div>
</body>
</html>
```